Brochure Design Project for Home Watch company

We are a new start up company in fast growing home watch industry. We provide services in Hawaii so the design needs to be reflect that. Our web site can give you overview of what we do - www.palmcrestkeeper.com. We will service clients that own second homes in Hawaii. These properties are not necessarily income producing properties for our clients. I'm looking for 2 or 4 page brochure which will be used to market our services to potential new clients. It needs to be high quality, modern with slight Hawaiian feel (we are based on Oahu). I'm not looking for a trifold type of brochure.

We are open to various colors based on what the designer might suggest but as you can see on our home page - the main picture of the home on our site has lots of red and white which we like as well as the "head" or dot above the "i" in our logo is red. I was not able to upload the file of the main house (purchased on snapvaultpix) on here therefore I'll have to provide the original photo to the selected designer at the later time. For now I just uploaded the not purchased copy.

If you have other questions please do let me know. And lastly, I will be looking to create a business card and post card as well.

```html
<!DOCTYPE html>
<html lang="en">
<head>
<meta charset="UTF-8">
<title>Palm Crest Keeper – Brochure</title>
<link rel="stylesheet" href="https://fonts.googleapis.com/css2?family=Questrial&family=Montserrat:wght@400;600;700&display=swap">
<style>
  :root {
    --bg-top: #f4f4f4;
    --bg-bottom: #d9d9d9;
    --paper: #ffffff;
    --ink: #2b2b2b;
    --muted: #8a8a8a;
    --accent-red: #e5484d;
    --sky-top: #2f6db5;
    --sky-mid: #4f88c9;
    --cover-photo-light: #6e9fd3;
    --cover-photo-deep: #2c5f95;
    --aerial-dark: #1f2b26;
    --aerial-mid: #3d5447;
    --band-grey: #ececec;
  }
  * { box-sizing: border-box; margin: 0; padding: 0; }
  html, body { width: 960px; height: 1200px; overflow: hidden; }
  body {
    background: linear-gradient(180deg, var(--bg-top), var(--bg-bottom));
    font-family: "Questrial", "Century Gothic", sans-serif;
    color: var(--ink);
    position: relative;
  }
  .spread {
    position: absolute;
    left: 50px;
    width: 860px;
    height: 556px;
    display: flex;
    box-shadow: 0 14px 30px rgba(0,0,0,0.18);
  }
  .spread--outside { top: 28px; }
  .spread--inside { top: 616px; }
  .page { position: relative; width: 430px; height: 100%; background: var(--paper); overflow: hidden; }
  .page + .page { border-left: 1px solid #e2e2e2; }

  /* Back cover */
  .back-cover__brand {
    position: absolute; top: 170px; left: 0; right: 0; text-align: center;
    font-family: "Montserrat", sans-serif; font-weight: 700; font-size: 18px; color: var(--ink);
    display: flex; justify-content: center; align-items: center; gap: 8px;
  }
  .brand-dot { width: 10px; height: 10px; border-radius: 50%; background: var(--accent-red); display: inline-block; }
  .back-cover__tagline { position: absolute; top: 198px; width: 100%; text-align: center; font-size: 10px; color: var(--muted); font-style: italic; }
  .back-cover__contact { position: absolute; top: 236px; width: 100%; text-align: center; font-size: 13px; line-height: 24px; letter-spacing: .3px; font-style: normal; }
  .back-cover__note { position: absolute; top: 368px; left: 210px; width: 190px; font-size: 8.5px; line-height: 12px; color: var(--muted); font-style: italic; }
  .back-cover__band { position: absolute; bottom: 0; left: 0; right: 0; height: 92px; background: var(--band-grey); }
  .accreditation-badge { position: absolute; left: 40px; top: 28px; width: 120px; height: 36px; border-radius: 4px; background: #c8ccd6; }

  /* Front cover */
  .front-cover { background: linear-gradient(180deg, var(--sky-top) 0%, var(--sky-mid) 100%); }
  .front-cover__brand {
    position: absolute; top: 44px; width: 100%; text-align: center;
    font-family: "Montserrat", sans-serif; font-weight: 700; font-size: 18px; color: #fff;
    display: flex; justify-content: center; align-items: center; gap: 8px;
  }
  .front-cover__tagline { position: absolute; top: 72px; width: 100%; text-align: center; font-size: 10px; color: #fff; }
  .front-cover__photo {
    position: absolute; top: 150px; left: 0; right: 0; bottom: 0;
    background: linear-gradient(180deg, var(--cover-photo-light) 0%, var(--cover-photo-deep) 100%);
  }
  .front-cover__title {
    position: absolute; top: 300px; left: 150px; width: 246px; padding: 14px 16px;
    border: 1.5px solid #fff; color: #fff; font-family: "Montserrat", sans-serif; font-weight: 600;
    font-size: 17px; line-height: 22px; text-align: center;
  }

  /* Inside left */
  .services-intro__heading { position: absolute; top: 36px; left: 30px; font-size: 24px; font-weight: 400; color: var(--accent-red); }
  .services-intro__text { position: absolute; top: 70px; left: 30px; width: 370px; font-size: 10px; line-height: 14px; }
  .house-illustration {
    position: absolute; top: 116px; left: 80px; width: 270px; height: 150px;
    background: linear-gradient(180deg, #f3f3f3, #d4d4d4); border-radius: 4px;
  }
  .service-block { position: absolute; font-size: 9.5px; line-height: 13px; }
  .service-block h3 { color: var(--accent-red); font-family: "Montserrat", sans-serif; font-weight: 600; font-size: 11px; line-height: 13px; margin-bottom: 6px; }
  .service-block--outdoor { top: 290px; left: 30px; width: 180px; }
  .service-block--exterior { top: 290px; left: 225px; width: 180px; }
  .service-block--interior { top: 420px; left: 30px; width: 370px; }
  .page-stripe { position: absolute; bottom: 0; left: 0; right: 0; height: 8px; background: var(--accent-red); }

  /* Inside right */
  .aerial-photo {
    position: absolute; top: 0; left: 0; right: 0; height: 150px;
    background: radial-gradient(ellipse at 40% 40%, var(--aerial-mid), var(--aerial-dark) 75%);
  }
  .aerial-photo__caption {
    position: absolute; top: 44px; left: 40px; width: 350px; padding: 10px 14px;
    border: 1px solid #fff; color: #fff; font-size: 10px; line-height: 14px;
  }
  .concierge-block { position: absolute; font-size: 9px; line-height: 12.5px; text-align: justify; }
  .concierge-block__label { color: var(--muted); font-size: 8px; }
  .concierge-block h3 { color: var(--accent-red); font-family: "Montserrat", sans-serif; font-weight: 600; font-size: 13px; margin-bottom: 5px; }
  .concierge-block--arrival { top: 170px; left: 30px; width: 175px; }
  .concierge-block--departure { top: 170px; left: 225px; width: 175px; }
  .concierge-block--special { top: 360px; left: 30px; width: 370px; }
  .concierge-block--special h3 { font-size: 15px; }
</style>
</head>
<body>

<section class="spread spread--outside">
  <article class="page back-cover">
    <div class="back-cover__brand"><span>Palm Crest Keeper</span><span class="brand-dot"></span></div>
    <p class="back-cover__tagline">Your Home Watch Company</p>
    <address class="back-cover__contact">
      Palm Crest Keeper LLC Honolulu Hawaii<br>
      808-555-0142<br>
      hello@palmcrestkeeper.com<br>
      www.palmcrestkeeper.com
    </address>
    <p class="back-cover__note">We are Accredited Members of the CHCG. We are insured and bonded, and we agreed to uphold the strictest and most ethical standards in the industry</p>
    <div class="back-cover__band">
      <div class="accreditation-badge" role="img" aria-label="Accreditation badge"></div>
    </div>
  </article>

  <article class="page front-cover">
    <div class="front-cover__brand"><span>Palm Crest Keeper</span><span class="brand-dot"></span></div>
    <p class="front-cover__tagline">Your Home Watch Company</p>
    <div class="front-cover__photo" role="img" aria-label="Photo of a tropical villa beside an infinity pool with palm trees and ocean view"></div>
    <h1 class="front-cover__title">Providing Premiere Home Watch and Concierge Services</h1>
  </article>
</section>

<section class="spread spread--inside">
  <article class="page services-page">
    <h2 class="services-intro__heading">What do we do?</h2>
    <p class="services-intro__text">We save your time. We perform visual inspections and provide our presence while you are away so you can enjoy your time and home while you are on the island. We have your back!</p>
    <div class="house-illustration" role="img" aria-label="Illustration of a house cross-section with inspection icons around it"></div>

    <div class="service-block service-block--outdoor">
      <h3>General Outdoor Visual Inspections</h3>
      <p>Check yard, lawn and landscaping; check lanai, deck, and pool area for any damage; check for mold or fading of all outdoor furniture; check water level of swimming pool or hot tub, if applicable</p>
    </div>
    <div class="service-block service-block--exterior">
      <h3>Home Exterior Visual Inspections</h3>
      <p>Check security cameras; check for overall damage; remove mail, newspapers, and flyers from mailbox and store inside of the property; check outdoor plumbing and hoses for leakage; check garage; check for vandalism and theft</p>
    </div>
    <div class="service-block service-block--interior">
      <h3>Home Interior Visual Inspections</h3>
      <p>Make sure security system is in working order; ensure that all doors, windows and sliders are locked and secured; check thermostats and make sure the air conditioning is set at appropriate and requested temperature; make sure all smoke detectors are in proper working order or replace batteries if necessary; visually inspect the water heater and washer and dryer</p>
    </div>
    <div class="page-stripe"></div>
  </article>

  <article class="page concierge-page">
    <div class="aerial-photo" role="img" aria-label="Aerial photo of an island coastline with green hills and homes">
      <p class="aerial-photo__caption">Don't let repairs or unexpected surprises upon your arrival take away from your vacation time. Arrive knowing all you need to do in Hawaii is relax and enjoy your second home and the island.</p>
    </div>

    <div class="concierge-block concierge-block--arrival">
      <p class="concierge-block__label">Concierge Services</p>
      <h3>Pre-Arrival</h3>
      <p>Groceries purchased and stored, air conditioning and ceiling vents turned on and/or windows opened, water turned on, flowers placed, fresh laundered linens on beds, towels arranged in the bathrooms, deck furniture placed on decks and patio, house freshened up and aired out, security system disarmed as appropriate, decks, walkways, lanais, and driveways cleaned of debris and special requests completed.</p>
    </div>
    <div class="concierge-block concierge-block--departure">
      <p class="concierge-block__label">Concierge Services</p>
      <h3>Post-Departure</h3>
      <p>House cleaning coordinated, beds made, sheets and towels cleaned, dishes washed and put away, all doors and windows secured, lights on timers set, water turned off, outdoor furniture stored or covered per specific instructions, driveways, lanais, walkways and decks cleared of debris, air conditioning set to appropriate level, trash placed for collection and security system turned on.</p>
    </div>
    <div class="concierge-block concierge-block--special">
      <p class="concierge-block__label">Concierge Services</p>
      <h3>Sample of Special Services/Requests</h3>
      <p>Key holding services, mail forwarding, coordination of transportation from and to the airport, light handyman and landscaping services, vendor coordination (we coordinate access and meet everyone you authorize at your home including but not limited to maintenance, repair, pest control, landscaping and tree trimming, and utility providers), pre-storm services (secure outdoor furniture, potted plants, hammocks and any other outdoor items, etc.) and post-storm services (clean walkway and driveway, pick-up trash, etc.), and emergency services response, etc. Additional services and pricing available upon request.</p>
    </div>
    <div class="page-stripe"></div>
  </article>
</section>

</body>
</html>
```